Construction machinery rental / heavy equipment rental needs a nice billboard

We need a billboard for our company.
We rent out construction machinery such as excavators, wheel loaders, wheel dumpers and so on...

I would like an elegant, simple, dark design.
Colors: black yellow grey white

The following must be on the billboard:
Logo
phone number: 078 / 513 90 41
website: www.kiesgrube-talwerk.ch
the machines I rent out: Bagger bis 10T, Radlader, Dumper, Raupenkipper

the font in the logo is: Square 721

Final format 2950 x 1900mm
I have uploaded pictures:
"Excavator 1-6" are my pictures, which can be used
"Sample 1-4" are pictures whose style I like
"Billboard" are billboards which I like

Requirements
Must have
• The following must be on the billboard: Logo phone number: 078 / 513 90 41 website: www.kiesgrube-talwerk.ch the machines I rent out: Bagger bis 10T, Radlader, Dumper, Raupenkipper

```html
<!DOCTYPE html>
<html lang="de">
<head>
<meta charset="utf-8">
<title>Talwerk Baumaschinenvermietung – Plakat</title>
<link rel="stylesheet" href="https://fonts.googleapis.com/css2?family=Bebas+Neue&family=Montserrat:wght@800&display=swap">
<style>
  :root{
    --black:#111111;
    --yellow:#f5cf1f;
    --yellow-deep:#c9a00f;
    --white:#ffffff;
    --pale:#dde6f2;
    --ink:#121212;
    --grey:#d9d9d9;
  }
  *{margin:0;padding:0;box-sizing:border-box}
  html,body{width:1200px;height:857px;overflow:hidden;background:var(--black)}
  .billboard{position:relative;width:1200px;height:857px;background:var(--black);overflow:hidden;font-family:"Bebas Neue",sans-serif}
  .photo{position:absolute;left:500px;top:190px;width:700px;height:580px;
    background:
      radial-gradient(ellipse at 88% 52%, rgba(255,255,255,.55) 0%, rgba(120,100,80,.25) 14%, transparent 32%),
      radial-gradient(ellipse at 60% 80%, #4a3a2a 0%, #2a2119 40%, transparent 75%),
      linear-gradient(90deg, var(--black) 0%, #1c1813 30%, #2b241c 70%, #1a1612 100%);}
  .corner{position:absolute;right:0;top:0}
  .brand{position:absolute;left:60px;top:80px;display:flex;align-items:center;gap:22px}
  .brand-mark{width:34px;height:34px;background:var(--yellow)}
  .brand-name{font-size:150px;line-height:1;color:var(--yellow);letter-spacing:6px}
  .headline{position:absolute;left:60px;top:300px;font-size:46px;color:var(--grey);letter-spacing:1px}
  .rule{position:absolute;left:0;top:362px;width:600px;height:3px;background:linear-gradient(90deg,var(--yellow-deep),var(--yellow-deep) 80%,transparent)}
  .machines{position:absolute;left:70px;top:395px;display:grid;grid-template-columns:260px 260px;row-gap:14px;list-style:none}
  .machines li{font-size:40px;color:var(--white);display:flex;align-items:center;gap:18px;line-height:1.1}
  .machines li::before{content:"";width:14px;height:14px;border-radius:50%;background:var(--yellow);flex:none}
  .footer{position:absolute;left:0;bottom:0}
  .phone{position:absolute;left:60px;top:740px;display:flex;align-items:center;gap:28px}
  .phone-icon{width:60px;height:60px;border-radius:50%;background:var(--white);display:flex;align-items:center;justify-content:center;box-shadow:0 4px 0 rgba(0,0,0,.25)}
  .phone-number{font-family:"Montserrat",sans-serif;font-weight:800;font-size:60px;color:var(--ink);letter-spacing:1px}
  .website{position:absolute;right:70px;top:790px;font-size:48px;color:var(--ink);letter-spacing:.5px}
</style>
</head>
<body>
<main class="billboard">
  <div class="photo" role="img" aria-label="Nachtaufnahme eines Minibaggers mit Scheinwerfern, der einen Graben aushebt"></div>

  <svg class="corner" width="190" height="220" viewBox="0 0 190 220" aria-hidden="true">
    <polygon points="0,0 190,0 190,220" fill="var(--yellow)"/>
  </svg>

  <div class="brand">
    <span class="brand-name">TALWERK</span>
    <span class="brand-mark"></span>
  </div>

  <h1 class="headline">Mieten Sie die passende Baumaschine</h1>
  <div class="rule"></div>

  <ul class="machines">
    <li>Bagger bis 10T</li>
    <li>Dumper</li>
    <li>Radlader</li>
    <li>Raupenkipper</li>
  </ul>

  <svg class="footer" width="1200" height="160" viewBox="0 0 1200 160" aria-hidden="true">
    <rect x="0" y="70" width="1200" height="90" fill="var(--pale)"/>
    <rect x="0" y="70" width="1200" height="40" fill="var(--white)"/>
    <path d="M0,0 L560,0 Q600,0 620,40 L680,160 L0,160 Z" fill="var(--yellow)"/>
    <path d="M0,110 L650,110 L680,160 L0,160 Z" fill="var(--yellow-deep)" opacity=".55"/>
  </svg>

  <div class="phone">
    <span class="phone-icon">
      <svg width="32" height="32" viewBox="0 0 24 24" aria-hidden="true">
        <path fill="#d9a514" d="M6.6 10.8a15.1 15.1 0 0 0 6.6 6.6l2.2-2.2c.3-.3.7-.4 1-.2 1.1.4 2.3.6 3.6.6.6 0 1 .4 1 1V20c0 .6-.4 1-1 1A17 17 0 0 1 3 4c0-.6.4-1 1-1h3.5c.6 0 1 .4 1 1 0 1.3.2 2.5.6 3.6.1.3 0 .7-.2 1z"/>
      </svg>
    </span>
    <span class="phone-number">078 / 513 90 41</span>
  </div>

  <p class="website">WWW.KIESGRUBE-TALWERK.CH</p>
</main>
</body>
</html>
```